Business Card + Stationary
TBV Financial Group
Professional
Dale Morrow
Business Development Manager
2718 SW 9th Ave. Suite 1146
Cedarview, WA 98000 Toll Free
dale@tbvfinancialgroup.example
www.tbvfinancialgroup.example
want to modernize & update website and design.
Feel free to update/ change TBV logo as you see fit.
Logo
More of a high res logo
eps logo
TBV Background (not sure if the quality is good enough though)

```html
<!DOCTYPE html>
<html lang="en">
<head>
<meta charset="utf-8">
<title>TBV Financial Group – Business Card</title>
<link rel="stylesheet" href="https://fonts.googleapis.com/css2?family=Libre+Baskerville:wght@400;700&family=Open+Sans:wght@400;600&display=swap">
<style>
  :root {
    --navy: #1f4f93;
    --navy-deep: #163b70;
    --ink: #1b1b1b;
    --paper: #ffffff;
    --stage: #e6e7ea;
    --muted: #4a4a4a;
    --rule: #bbbbbb;
  }
  * { margin: 0; padding: 0; box-sizing: border-box; }
  html, body { width: 1200px; height: 864px; overflow: hidden; }
  body {
    background: var(--stage);
    font-family: "Open Sans", Arial, sans-serif;
    display: flex;
    align-items: center;
    justify-content: center;
    gap: 50px;
  }
  .card {
    position: relative;
    width: 540px;
    height: 309px;
    border-radius: 22px;
    overflow: hidden;
    box-shadow: 0 6px 18px rgba(0,0,0,.18);
  }
  /* Back */
  .card-back {
    background: var(--navy);
    color: var(--paper);
  }
  .back-mark {
    position: absolute;
    top: 100px; left: 0; right: 0;
    display: flex; flex-direction: column; align-items: center; gap: 12px;
  }
  .back-mark .dot {
    width: 46px; height: 46px; border-radius: 50%;
    background: var(--paper);
  }
  .back-mark .name {
    font-family: "Libre Baskerville", Georgia, serif;
    font-weight: 700; font-size: 20px; letter-spacing: 1px;
  }
  .back-web {
    position: absolute; bottom: 40px; left: 0; right: 0;
    text-align: center; font-size: 14px; letter-spacing: 3px;
  }
  /* Front */
  .card-front { background: var(--paper); color: var(--ink); }
  .front-swoosh { position: absolute; inset: 0; }
  .front-brand {
    position: absolute; top: 46px; left: 110px;
    display: flex; align-items: center; gap: 12px;
  }
  .front-brand .square {
    width: 38px; height: 38px; background: var(--navy);
  }
  .front-brand .name {
    font-family: "Libre Baskerville", Georgia, serif;
    font-weight: 700; font-size: 24px; color: var(--ink);
  }
  .front-details {
    position: absolute; top: 120px; left: 80px;
    display: flex; gap: 18px; font-size: 11px; color: var(--muted);
  }
  .person { text-align: right; line-height: 1.55; padding-right: 18px; border-right: 1px solid var(--rule); }
  .person .person-name { color: var(--navy); font-weight: 600; font-size: 13px; }
  .person .address { margin-top: 14px; }
  .contacts { list-style: none; line-height: 1.9; }
  .contacts li { display: flex; align-items: center; gap: 7px; }
  .contacts svg { width: 12px; height: 12px; flex: none; }
</style>
</head>
<body>

<section class="card card-back">
  <div class="back-mark">
    <span class="dot"></span>
    <span class="name">TBV Financial Group</span>
  </div>
  <p class="back-web">www.tbvfinancialgroup.example</p>
</section>

<section class="card card-front">
  <svg class="front-swoosh" viewBox="0 0 540 309" preserveAspectRatio="none" aria-hidden="true">
    <path d="M230 309 C360 280 470 220 540 130 L540 309 Z" fill="var(--ink)"/>
    <path d="M270 309 C390 285 480 235 540 165 L540 309 Z" fill="#ffffff"/>
    <path d="M300 309 C410 290 490 250 540 195 L540 309 Z" fill="var(--navy)"/>
    <path d="M420 309 C470 295 510 270 540 245 L540 309 Z" fill="var(--navy-deep)"/>
  </svg>

  <div class="front-brand">
    <span class="square"></span>
    <span class="name">TBV Financial Group</span>
  </div>

  <div class="front-details">
    <div class="person">
      <p class="person-name">Dale Morrow</p>
      <p class="role">Business Development Manager</p>
      <p class="address">2718 SW 9th Ave. Suite 1146<br>Cedarview, WA 98000 Toll Free</p>
    </div>
    <ul class="contacts">
      <li>
        <svg viewBox="0 0 12 12"><circle cx="6" cy="6" r="6" fill="var(--navy)"/><path d="M4 3l1.2 1.6-.7.8c.4.9 1.1 1.6 2 2l.8-.7L9 8l-.6 1C6 9 3 6 3 3.6z" fill="#fff"/></svg>
        866.555.0142
      </li>
      <li>
        <svg viewBox="0 0 12 12"><circle cx="6" cy="6" r="6" fill="var(--navy)"/><rect x="3" y="4" width="6" height="4" fill="none" stroke="#fff" stroke-width=".8"/><path d="M3 4l3 2.2L9 4" fill="none" stroke="#fff" stroke-width=".8"/></svg>
        dale@tbvfinancialgroup.example
      </li>
      <li>
        <svg viewBox="0 0 12 12"><circle cx="6" cy="6" r="6" fill="var(--navy)"/><circle cx="6" cy="6" r="3" fill="none" stroke="#fff" stroke-width=".8"/><path d="M3 6h6M6 3v6" stroke="#fff" stroke-width=".6"/></svg>
        www.tbvfinancialgroup.example
      </li>
    </ul>
  </div>
</section>

</body>
</html>
```